Post Surgery Care Reminder App

Mobile app-based reminder for patients after surgery. Often times once the patient goes home, they are instructed to take medications and perform other care for their wounds. This app will be designed to help patients keep on top of their care to ensure optimal outcomes after their surgery. See the attached video link (clipnest) in the "Must Haves" section for example of our current beta version.

We have immediate room for improvements from the version in the video; looking for designer/coder to help us complete this project to move to consumers.

Target Market(s)

Patients undergoing elective surgeries

Industry/Entity Type

Health Care

Colors

Designer to choose colors to be used in the design.

Requirements
Must have
• Please see linked clipnest video for demonstration:
• https://www.clipnest.com/watch?v=pRaKe7Wq2bN
Nice to have
• Improved user interface: pleasing to the eye as well as smooth and easy to navigate experience.

```html
<!DOCTYPE html>
<html lang="en">
<head>
<meta charset="utf-8">
<title>Recova – Post Surgery Care Reminder Screens</title>
<link href="https://fonts.googleapis.com/css2?family=Oswald:wght@300;400&family=Lato:wght@400;700&display=swap" rel="stylesheet">
<style>
:root{
  --sky-top:#6de6f9;
  --sky-mid:#a8dbf6;
  --sky-bottom:#c8c2f5;
  --brand:#1e88d8;
  --brand-dark:#1a6fb5;
  --white:#ffffff;
  --ink:#333a40;
  --muted:#8a929a;
  --night:#232729;
  --night-panel:#2b2f32;
  --night-soft:#3a3f43;
  --star:#f5a623;
  --gem:#3ec46d;
  --page:#ffffff;
}
*{box-sizing:border-box;margin:0;padding:0}
html,body{width:912px;height:1200px;overflow:hidden;background:var(--page)}
.board{position:relative;width:912px;height:1200px}

/* screen: authored at 219×389, scaled onto the board */
.screen{position:absolute;width:219px;height:389px;transform-origin:0 0;transform:scale(.5429);overflow:hidden;
  background:linear-gradient(180deg,var(--sky-top) 0%,var(--sky-mid) 55%,var(--sky-bottom) 100%);
  font-family:"Lato",sans-serif;color:var(--ink)}
.screen.dark{background:var(--night)}

.status{position:absolute;top:3px;right:6px;display:flex;align-items:center;gap:3px;font-size:8px;color:#222}
.dark .status{color:#555}
.status svg{display:block}

.logo{position:absolute;left:84px;top:24px;width:52px;height:52px;border-radius:50%;background:var(--white);
  display:flex;align-items:center;justify-content:center;font-family:"Oswald",sans-serif;font-weight:400;font-size:11px;color:var(--brand)}
.dark .logo{background:#2f2b2b;color:#4a4444}

.nav{position:absolute;left:0;right:0;bottom:8px;height:12px}
.nav svg{position:absolute;top:0}

.card{position:absolute;left:15px;width:190px;background:var(--white)}
.card.blue{background:var(--brand);color:var(--white)}
.card.framed{border:3px solid var(--brand)}

.btn{position:absolute;height:22px;border-radius:12px;background:var(--brand);color:var(--white);
  font-size:7px;font-weight:700;display:flex;align-items:center;justify-content:center;box-shadow:0 1px 2px rgba(0,0,0,.15)}
.btn.light{background:var(--white);color:var(--brand)}
.btn.wide{left:15px;width:190px}
.btn.prev{left:38px;width:74px}
.btn.next{left:118px;width:62px}
.btn.solo{left:79px;width:62px}
.btn.ghost{background:#27415a;color:#3e5a72;box-shadow:none}

.title{position:absolute;left:8px;right:8px;top:92px;text-align:center;font-family:"Oswald",sans-serif;font-weight:300;
  font-size:19px;line-height:1.22;color:var(--brand)}

.idle-text{position:absolute;left:0;right:0;bottom:9px;text-align:center;font-family:"Oswald",sans-serif;font-weight:300;font-size:11px;color:var(--brand)}
.blue .idle-text{color:var(--white)}
.idle-icon{position:absolute;left:72px;top:12px}

.tile{position:absolute;top:226px;width:88px;height:128px;background:var(--white)}
.tile.drain{left:15px}
.tile.pills{left:117px}
.tile.active{border:2px solid var(--brand)}
.tile svg{position:absolute;left:19px;top:20px}
.tile span{position:absolute;left:4px;right:4px;top:90px;text-align:center;font-family:"Oswald",sans-serif;font-weight:300;font-size:9.5px;line-height:1.25;color:var(--brand)}
.tile.faded svg,.tile.faded span{opacity:.3}

.choice{position:absolute;width:52px;height:52px;border-radius:50%;border:3px solid var(--white);display:flex;align-items:center;justify-content:center;
  font-family:"Oswald",sans-serif;font-size:19px;color:var(--white)}
.choice.on{background:var(--brand);border-width:4px}
.choice.off{background:transparent;opacity:.8}

.field{position:absolute;left:80px;width:60px;height:20px;background:var(--white);font-size:7px;display:flex;align-items:center;justify-content:center}
.caption{position:absolute;left:0;right:0;text-align:center;font-family:"Oswald",sans-serif;font-size:12px;color:#1d2328}

.dim-panel{position:absolute;left:15px;width:190px;background:var(--night-panel)}

.dialog-title{text-align:center;font-family:"Oswald",sans-serif;font-weight:300;font-size:10px;color:var(--brand);margin-top:14px}
.blue .dialog-title{color:var(--white)}
.dialog-body{text-align:center;font-size:6.2px;line-height:1.35;color:var(--muted);padding:8px 18px 0}
.blue .dialog-body{color:var(--white)}
.dialog-actions{position:absolute;left:0;right:0;bottom:8px;height:22px}
.dialog-actions .btn{top:0}

.summary{text-align:center;font-size:8px;line-height:1.32;color:var(--white);padding-top:12px}

.clock{position:absolute;left:0;right:0;top:14px;text-align:center;font-size:34px;color:var(--white);letter-spacing:1px}
.clock small{font-size:8px;vertical-align:middle;opacity:.8}

.picker-row{position:absolute;left:15px;right:15px;font-size:6px;color:var(--ink)}
.radio{display:inline-block;width:7px;height:7px;border-radius:50%;border:1.4px solid #333;vertical-align:middle;margin-right:4px;position:relative}
.radio.on::after{content:"";position:absolute;left:1px;top:1px;width:2px;height:2px;border-radius:50%;background:#333}

.reward-sheet{position:absolute;left:15px;top:86px;width:190px;height:216px;background:var(--white)}
.reward-sheet svg{position:absolute;top:16px}

.splash-ring{position:absolute;left:56px;top:140px;width:108px;height:108px;border-radius:50%;background:var(--white);
  display:flex;align-items:center;justify-content:center;font-family:"Oswald",sans-serif;font-size:18px;color:var(--brand);box-shadow:0 2px 10px rgba(0,0,0,.2)}
.screen.splash{background:linear-gradient(180deg,#7ae4f8 0%,#64b9ee 60%,#4a94e3 100%)}
</style>
</head>
<body>
<div class="board">

<!-- Row 1 -->
<section class="screen" style="left:38.5px;top:29.3px">
  <div class="status"><svg width="22" height="7"><path d="M0 1h8L4 6z" fill="#222"/><path d="M10 6h5V1z" fill="#222"/><rect x="17" y="0" width="4" height="7" fill="#222"/></svg>12:30</div>
  <div class="logo">Recova</div>
  <div class="card" style="top:86px;height:96px">
    <svg class="idle-icon" width="76" height="56" viewBox="0 0 76 56"><path d="M38 8a20 20 0 0 1 20 20H38" fill="none" stroke="#1e88d8" stroke-width="4"/><g fill="#1e88d8"><circle cx="20" cy="28" r="2"/><circle cx="24" cy="17" r="2"/><circle cx="32" cy="10" r="2"/><circle cx="24" cy="40" r="2"/><circle cx="38" cy="46" r="2"/><circle cx="52" cy="40" r="2"/></g></svg>
    <p class="idle-text">Nothing to do at the moment.</p>
  </div>
  <div class="btn wide" style="top:191px">View Reponses</div>
  <div class="tile drain active"><svg width="50" height="50"><rect x="2" y="2" width="46" height="46" rx="4" fill="none" stroke="#1e88d8" stroke-width="3"/><g stroke="#1e88d8" stroke-width="3"><path d="M10 12h30M10 20h30M10 28h30M10 36h30"/></g></svg><span>Remind me to strip my drains</span></div>
  <div class="tile pills"><svg width="50" height="50"><rect x="2" y="14" width="26" height="14" rx="7" transform="rotate(40 15 21)" fill="#1e88d8"/><rect x="20" y="8" width="28" height="14" rx="7" transform="rotate(-40 34 15)" fill="#1e88d8"/><g fill="#1e88d8"><circle cx="24" cy="34" r="3"/><circle cx="18" cy="42" r="2.5"/><circle cx="30" cy="42" r="2.5"/><circle cx="24" cy="47" r="2"/></g></svg><span>Remind me to take my antibiotics</span></div>
  <div class="nav"><svg width="219" height="12"><path d="M44 6l8-5v10z" fill="none" stroke="#222" stroke-width="1.4"/><circle cx="110" cy="6" r="5" fill="none" stroke="#222" stroke-width="1.4"/><rect x="166" y="1" width="10" height="10" fill="none" stroke="#222" stroke-width="1.4"/></svg></div>
</section>

<section class="screen" style="left:181.9px;top:29.3px">
  <div class="status"><svg width="22" height="7"><path d="M0 1h8L4 6z" fill="#222"/><path d="M10 6h5V1z" fill="#222"/><rect x="17" y="0" width="4" height="7" fill="#222"/></svg>12:30</div>
  <div class="logo">Recova</div>
  <div class="card framed" style="top:86px;height:98px;background:#eee">
    <div style="background:#fff;height:26px;padding:8px 6px;font-size:6.5px">Abcdef</div>
    <div style="padding:6px 6px;font-size:5.5px;line-height:2.4"><b>- 2018 - 06 - 02</b><br><span style="color:#999">- 2018 - 06 - 03</span></div>
    <div style="position:absolute;left:0;right:0;bottom:0;height:20px;background:var(--brand);color:#fff;font-size:6px;display:flex;align-items:center;padding-left:6px;gap:16px"><span><span class="radio" style="border-color:#fff"></span>08:00</span><span><span class="radio on" style="border-color:#fff"></span>Initial Alarm</span></div>
  </div>
  <div class="btn wide" style="top:190px">Add Anither Alarm</div>
  <div class="btn wide light" style="top:225px">Create</div>
  <div class="nav"><svg width="219" height="12"><path d="M44 6l8-5v10z" fill="none" stroke="#222" stroke-width="1.4"/><circle cx="110" cy="6" r="5" fill="none" stroke="#222" stroke-width="1.4"/><rect x="166" y="1" width="10" height="10" fill="none" stroke="#222" stroke-width="1.4"/></svg></div>
</section>

<section class="screen dark" style="left:324.7px;top:29.3px">
  <div class="status"><svg width="22" height="7"><path d="M0 1h8L4 6z" fill="#555"/><path d="M10 6h5V1z" fill="#555"/><rect x="17" y="0" width="4" height="7" fill="#555"/></svg>12:30</div>
  <div class="logo">Recova</div>
  <div class="card blue" style="top:86px;height:132px">
    <div class="clock"><small>⁝ </small>10 : 24<small> ⁝</small></div>
    <div style="position:absolute;left:0;right:0;bottom:0;height:52px;background:var(--brand-dark)"></div>
    <svg style="position:absolute;left:16px;top:100px" width="14" height="9"><rect width="14" height="9" rx="1" fill="#cfe6f8"/></svg>
    <div class="btn light" style="left:44px;top:94px;width:62px">Cancel</div>
    <div class="btn light" style="left:112px;top:94px;width:62px">OK</div>
  </div>
  <div class="btn ghost wide" style="top:225px">Create</div>
  <div class="nav"><svg width="219" height="12"><path d="M44 6l8-5v10z" fill="none" stroke="#555" stroke-width="1.4"/><circle cx="110" cy="6" r="5" fill="none" stroke="#555" stroke-width="1.4"/><rect x="166" y="1" width="10" height="10" fill="none" stroke="#555" stroke-width="1.4"/></svg></div>
</section>

<section class="screen" style="left:468px;top:29.3px">
  <div class="status"><svg width="22" height="7"><path d="M0 1h8L4 6z" fill="#222"/><path d="M10 6h5V1z" fill="#222"/><rect x="17" y="0" width="4" height="7" fill="#222"/></svg>12:30</div>
  <div class="logo">Recova</div>
  <div class="card blue" style="top:86px;height:96px">
    <svg class="idle-icon" width="76" height="56" viewBox="0 0 76 56"><path d="M38 8a20 20 0 0 1 20 20H38" fill="none" stroke="#fff" stroke-width="4"/><g fill="#fff"><circle cx="20" cy="28" r="2"/><circle cx="24" cy="17" r="2"/><circle cx="32" cy="10" r="2"/><circle cx="24" cy="40" r="2"/><circle cx="38" cy="46" r="2"/><circle cx="52" cy="40" r="2"/></g></svg>
    <p class="idle-text">Nothing to do at the moment.</p>
  </div>
  <div class="btn wide light" style="top:191px">View Reponses</div>
  <div class="tile drain faded"><svg width="50" height="50"><rect x="2" y="2" width="46" height="46" rx="4" fill="none" stroke="#1e88d8" stroke-width="3"/><g stroke="#1e88d8" stroke-width="3"><path d="M10 12h30M10 20h30M10 28h30M10 36h30"/></g></svg><span>Remind me to strip my drains</span></div>
  <div class="tile pills"><svg width="50" height="50"><rect x="2" y="14" width="26" height="14" rx="7" transform="rotate(40 15 21)" fill="#1e88d8"/><rect x="20" y="8" width="28" height="14" rx="7" transform="rotate(-40 34 15)" fill="#1e88d8"/><g fill="#1e88d8"><circle cx="24" cy="34" r="3"/><circle cx="18" cy="42" r="2.5"/><circle cx="30" cy="42" r="2.5"/><circle cx="24" cy="47" r="2"/></g></svg><span>Remind me to take my antibiotics</span></div>
  <div class="nav"><svg width="219" height="12"><path d="M44 6l8-5v10z" fill="none" stroke="#222" stroke-width="1.4"/><circle cx="110" cy="6" r="5" fill="none" stroke="#222" stroke-width="1.4"/><rect x="166" y="1" width="10" height="10" fill="none" stroke="#222" stroke-width="1.4"/></svg></div>
</section>

<section class="screen dark" style="left:611.3px;top:29.3px">
  <div class="status"><svg width="22" height="7"><path d="M0 1h8L4 6z" fill="#555"/><path d="M10 6h5V1z" fill="#555"/><rect x="17" y="0" width="4" height="7" fill="#555"/></svg>12:30</div>
  <div class="logo">Recova</div>
  <svg style="position:absolute;left:60px;top:218px" width="100" height="110"><path d="M0 0h100L62 100H38z" fill="#2b2f32"/></svg>
  <div class="card" style="top:86px;height:132px">
    <p class="dialog-title">Time to strip your drains</p>
    <p class="dialog-body">It is time to strip your drains. Please follow the instructions provided by your physician.</p>
    <div class="dialog-actions"><div class="btn" style="left:32px;width:62px">Snooze</div><div class="btn" style="left:100px;width:62px">Done</div></div>
  </div>
  <div class="btn ghost solo" style="top:330px">Next</div>
  <div class="nav"><svg width="219" height="12"><path d="M44 6l8-5v10z" fill="none" stroke="#555" stroke-width="1.4"/><circle cx="110" cy="6" r="5" fill="none" stroke="#555" stroke-width="1.4"/><rect x="166" y="1" width="10" height="10" fill="none" stroke="#555" stroke-width="1.4"/></svg></div>
</section>

<section class="screen" style="left:754.6px;top:29.3px">
  <div class="status"><svg width="22" height="7"><path d="M0 1h8L4 6z" fill="#222"/><path d="M10 6h5V1z" fill="#222"/><rect x="17" y="0" width="4" height="7" fill="#222"/></svg>12:30</div>
  <div class="logo">Recova</div>
  <h2 class="title" style="top:88px">How Difficult was it to strip the drain?</h2>
  <p class="caption" style="top:142px;font-family:Lato,sans-serif;font-size:5px;font-weight:700">Very Diffucult</p>
  <svg style="position:absolute;left:60px;top:152px" width="100" height="160">
    <defs><linearGradient id="effort" x1="0" y1="0" x2="0" y2="1"><stop offset="0" stop-color="#f39c12"/><stop offset=".45" stop-color="#5aa83a"/><stop offset="1" stop-color="#1c2a6e"/></linearGradient></defs>
    <path d="M10 8h80L74 80H26z" fill="#fff"/>
    <path d="M26 80h48L60 150H40z" fill="url(#effort)"/>
    <path d="M8 80h84" stroke="#222" stroke-width="1.2"/>
    <circle cx="50" cy="80" r="4" fill="#fff" stroke="#222" stroke-width="1.2"/>
  </svg>
  <p class="caption" style="top:312px;font-family:Lato,sans-serif;font-size:5px;font-weight:700">Very Easy</p>
  <div class="btn solo" style="top:330px">Next</div>
  <div class="nav"><svg width="219" height="12"><path d="M44 6l8-5v10z" fill="none" stroke="#222" stroke-width="1.4"/><circle cx="110" cy="6" r="5" fill="none" stroke="#222" stroke-width="1.4"/><rect x="166" y="1" width="10" height="10" fill="none" stroke="#222" stroke-width="1.4"/></svg></div>
</section>

<!-- Row 2 -->
<section class="screen" style="left:38.5px;top:262.2px">
  <div class="status"><svg width="22" height="7"><path d="M0 1h8L4 6z" fill="#222"/><path d="M10 6h5V1z" fill="#222"/><rect x="17" y="0" width="4" height="7" fill="#222"/></svg>12:30</div>
  <div class="logo">Recova</div>
  <h2 class="title">Did you experience any discomfort?</h2>
  <div class="choice on" style="left:84px;top:155px">Yes</div>
  <div class="choice off" style="left:84px;top:228px">No</div>
  <div class="btn prev" style="top:329px">Previous</div>
  <div class="btn next" style="top:329px">Next</div>
  <div class="nav"><svg width="219" height="12"><path d="M44 6l8-5v10z" fill="none" stroke="#222" stroke-width="1.4"/><circle cx="110" cy="6" r="5" fill="none" stroke="#222" stroke-width="1.4"/><rect x="166" y="1" width="10" height="10" fill="none" stroke="#222" stroke-width="1.4"/></svg></div>
</section>

<section class="screen" style="left:181.9px;top:262.2px">
  <div class="status"><svg width="22" height="7"><path d="M0 1h8L4 6z" fill="#222"/><path d="M10 6h5V1z" fill="#222"/><rect x="17" y="0" width="4" height="7" fill="#222"/></svg>12:30</div>
  <div class="logo">Recova</div>
  <h2 class="title">About how much fluid was in the bulb?</h2>
  <div class="field" style="top:200px">2</div>
  <p class="caption" style="top:240px;font-size:16px">CC's</p>
  <div class="btn prev" style="top:329px">Previous</div>
  <div class="btn next" style="top:329px">Next</div>
  <div class="nav"><svg width="219" height="12"><path d="M44 6l8-5v10z" fill="none" stroke="#222" stroke-width="1.4"/><circle cx="110" cy="6" r="5" fill="none" stroke="#222" stroke-width="1.4"/><rect x="166" y="1" width="10" height="10" fill="none" stroke="#222" stroke-width="1.4"/></svg></div>
</section>

<section class="screen" style="left:324.7px;top:262.2px">
  <div class="status"><svg width="22" height="7"><path d="M0 1h8L4 6z" fill="#222"/><path d="M10 6h5V1z" fill="#222"/><rect x="17" y="0" width="4" height="7" fill="#222"/></svg>12:30</div>
  <div class="logo">Recova</div>
  <h2 class="title">What is the general color of the fluid in the bulb?</h2>
  <div class="card" style="top:198px;height:22px;left:17px;width:185px;font-size:6.5px;padding:7px 12px">Pink<svg style="position:absolute;right:10px;top:8px" width="7" height="5"><path d="M1 1l2.5 3L6 1" fill="none" stroke="#222" stroke-width="1.3"/></svg></div>
  <div class="card" style="top:222px;height:54px;left:17px;width:185px;background:#e6e6e6;font-size:5px;line-height:2.7;padding:4px 12px;color:#555">- White<br><b style="color:#111">- Pink</b><br>- Red</div>
  <div class="btn prev" style="top:329px">Previous</div>
  <div class="btn next" style="top:329px">Complete</div>
  <div class="nav"><svg width="219" height="12"><path d="M44 6l8-5v10z" fill="none" stroke="#222" stroke-width="1.4"/><circle cx="110" cy="6" r="5" fill="none" stroke="#222" stroke-width="1.4"/><rect x="166" y="1" width="10" height="10" fill="none" stroke="#222" stroke-width="1.4"/></svg></div>
</section>

<section class="screen dark" style="left:468px;top:262.2px">
  <div class="status"><svg width="22" height="7"><path d="M0 1h8L4 6z" fill="#555"/><path d="M10 6h5V1z" fill="#555"/><rect x="17" y="0" width="4" height="7" fill="#555"/></svg>12:30</div>
  <div class="logo">Recova</div>
  <div class="card blue" style="top:86px;height:122px">
    <p class="dialog-title">Congratulations</p>
    <p class="dialog-body">You have earned another star!<br>Keep up the good work!</p>
    <svg style="position:absolute;left:89px;top:66px" width="12" height="12" viewBox="0 0 24 24"><path d="M12 1l3.2 7 7.6.8-5.7 5.1 1.6 7.5L12 17.6 5.3 21.4l1.6-7.5L1.2 8.8l7.6-.8z" fill="var(--star)"/></svg>
    <div class="dialog-actions"><div class="btn light" style="left:64px;width:62px">OK</div></div>
  </div>
  <div style="position:absolute;left:15px;top:222px;font-size:5px;line-height:2.6;color:#444">- White<br>- Pink<br>- Red</div>
  <div class="btn ghost prev" style="top:329px">Previous</div>
  <div class="btn ghost next" style="top:329px">Complete</div>
  <div class="nav"><svg width="219" height="12"><path d="M44 6l8-5v10z" fill="none" stroke="#555" stroke-width="1.4"/><circle cx="110" cy="6" r="5" fill="none" stroke="#555" stroke-width="1.4"/><rect x="166" y="1" width="10" height="10" fill="none" stroke="#555" stroke-width="1.4"/></svg></div>
</section>

<section class="screen" style="left:611.3px;top:262.2px">
  <div class="status"><svg width="22" height="7"><path d="M0 1h8L4 6z" fill="#222"/><path d="M10 6h5V1z" fill="#222"/><rect x="17" y="0" width="4" height="7" fill="#222"/></svg>12:30</div>
  <div class="logo">Recova</div>
  <div class="reward-sheet"><svg style="left:16px" width="24" height="24" viewBox="0 0 24 24"><path d="M12 1l3.2 7 7.6.8-5.7 5.1 1.6 7.5L12 17.6 5.3 21.4l1.6-7.5L1.2 8.8l7.6-.8z" fill="var(--star)"/></svg></div>
  <div class="nav"><svg width="219" height="12"><path d="M44 6l8-5v10z" fill="none" stroke="#222" stroke-width="1.4"/><circle cx="110" cy="6" r="5" fill="none" stroke="#222" stroke-width="1.4"/><rect x="166" y="1" width="10" height="10" fill="none" stroke="#222" stroke-width="1.4"/></svg></div>
</section>

<section class="screen dark" style="left:754.6px;top:262.2px">
  <div class="status"><svg width="22" height="7"><path d="M0 1h8L4 6z" fill="#555"/><path d="M10 6h5V1z" fill="#555"/><rect x="17" y="0" width="4" height="7" fill="#555"/></svg>12:30</div>
  <div class="logo">Recova</div>
  <div class="card blue" style="top:86px;height:122px">
    <p class="summary">06/02/2018 08:42PM EDT<br>Drain Care<br>Difficulty: 7<br>Discomfort: ture<br>Amount of Fluid: 5<br>Color: Pink</p>
    <div class="dialog-actions"><div class="btn light" style="left:64px;width:62px">OK</div></div>
  </div>
  <div class="dim-panel" style="top:208px;height:90px"></div>
  <div class="nav"><svg width="219" height="12"><path d="M44 6l8-5v10z" fill="none" stroke="#555" stroke-width="1.4"/><circle cx="110" cy="6" r="5" fill="none" stroke="#555" stroke-width="1.4"/><rect x="166" y="1" width="10" height="10" fill="none" stroke="#555" stroke-width="1.4"/></svg></div>
</section>

<!-- Row 3 -->
<section class="screen" style="left:38.5px;top:494.6px">
  <div class="status"><svg width="22" height="7"><path d="M0 1h8L4 6z" fill="#222"/><path d="M10 6h5V1z" fill="#222"/><rect x="17" y="0" width="4" height="7" fill="#222"/></svg>12:30</div>
  <div class="logo">Recova</div>
  <div class="card blue" style="top:86px;height:96px">
    <svg class="idle-icon" width="76" height="56" viewBox="0 0 76 56"><path d="M38 8a20 20 0 0 1 20 20H38" fill="none" stroke="#fff" stroke-width="4"/><g fill="#fff"><circle cx="20" cy="28" r="2"/><circle cx="24" cy="17" r="2"/><circle cx="32" cy="10" r="2"/><circle cx="24" cy="40" r="2"/><circle cx="38" cy="46" r="2"/><circle cx="52" cy="40" r="2"/></g></svg>
    <p class="idle-text">Nothing to do at the moment.</p>
  </div>
  <div class="btn wide light" style="top:191px">View Reponses</div>
  <div class="tile drain faded"><svg width="50" height="50"><rect x="2" y="2" width="46" height="46" rx="4" fill="none" stroke="#1e88d8" stroke-width="3"/><g stroke="#1e88d8" stroke-width="3"><path d="M10 12h30M10 20h30M10 28h30M10 36h30"/></g></svg><span>Remind me to strip my drains</span></div>
  <div class="tile pills"><svg width="50" height="50"><rect x="2" y="14" width="26" height="14" rx="7" transform="rotate(40 15 21)" fill="#1e88d8"/><rect x="20" y="8" width="28" height="14" rx="7" transform="rotate(-40 34 15)" fill="#1e88d8"/><g fill="#1e88d8"><circle cx="24" cy="34" r="3"/><circle cx="18" cy="42" r="2.5"/><circle cx="30" cy="42" r="2.5"/><circle cx="24" cy="47" r="2"/></g></svg><span>Remind me to take my antibiotics</span></div>
  <div class="nav"><svg width="219" height="12"><path d="M44 6l8-5v10z" fill="none" stroke="#222" stroke-width="1.4"/><circle cx="110" cy="6" r="5" fill="none" stroke="#222" stroke-width="1.4"/><rect x="166" y="1" width="10" height="10" fill="none" stroke="#222" stroke-width="1.4"/></svg></div>
</section>

<section class="screen" style="left:181.9px;top:494.6px">
  <div class="status"><svg width="22" height="7"><path d="M0 1h8L4 6z" fill="#222"/><path d="M10 6h5V1z" fill="#222"/><rect x="17" y="0" width="4" height="7" fill="#222"/></svg>12:30</div>
  <div class="logo">Recova</div>
  <h2 class="title">Medication Administration Instructions:</h2>
  <p class="caption" style="top:164px">Please take</p>
  <div class="field" style="top:202px">2</div>
  <p class="caption" style="top:262px">Tables with meals</p>
  <div class="btn solo" style="top:329px;left:80px;width:60px">Next</div>
  <div class="nav"><svg width="219" height="12"><path d="M44 6l8-5v10z" fill="none" stroke="#222" stroke-width="1.4"/><circle cx="110" cy="6" r="5" fill="none" stroke="#222" stroke-width="1.4"/><rect x="166" y="1" width="10" height="10" fill="none" stroke="#222" stroke-width="1.4"/></svg></div>
</section>

<section class="screen" style="left:324.7px;top:494.6px">
  <div class="status"><svg width="22" height="7"><path d="M0 1h8L4 6z" fill="#222"/><path d="M10 6h5V1z" fill="#222"/><rect x="17" y="0" width="4" height="7" fill="#222"/></svg>12:30</div>
  <div class="logo">Recova</div>
  <div class="card framed" style="top:86px;height:98px;background:#e6e6e6">
    <div style="background:#fff;height:24px;padding:8px 6px;font-size:6.5px">ev4</div>
    <div style="padding:4px 6px;font-size:5.5px"><b>- 2018 - 06 - 02</b></div>
    <div class="picker-row" style="top:44px;left:6px;color:#999"><span class="radio"></span>08:00 <span style="margin-left:20px"><span class="radio"></span>Initial Alarm</span></div>
    <div class="picker-row" style="top:57px;left:6px;color:#999"><span class="radio"></span>18:00 <span style="margin-left:20px"><span class="radio"></span>Initial Alarm</span></div>
    <div class="picker-row" style="top:70px;left:6px;color:#999"><span class="radio"></span>14:00 <span style="margin-left:20px"><span class="radio"></span>Initial Alarm</span></div>
  </div>
  <div class="btn wide light" style="top:190px">Add Anither Alarm</div>
  <div class="btn wide light" style="top:225px">Create</div>
  <div class="nav"><svg width="219" height="12"><path d="M44 6l8-5v10z" fill="none" stroke="#222" stroke-width="1.4"/><circle cx="110" cy="6" r="5" fill="none" stroke="#222" stroke-width="1.4"/><rect x="166" y="1" width="10" height="10" fill="none" stroke="#222" stroke-width="1.4"/></svg></div>
</section>

<section class="screen dark" style="left:468px;top:494.6px">
  <div class="status"><svg width="22" height="7"><path d="M0 1h8L4 6z" fill="#555"/><path d="M10 6h5V1z" fill="#555"/><rect x="17" y="0" width="4" height="7" fill="#555"/></svg>12:30</div>
  <div class="logo">Recova</div>
  <div class="card blue" style="top:86px;height:132px">
    <div class="clock"><small>⁝ </small>10 : 24<small> ⁝</small></div>
    <div style="position:absolute;left:0;right:0;bottom:0;height:52px;background:var(--brand-dark)"></div>
    <svg style="position:absolute;left:16px;top:100px" width="14" height="9"><rect width="14" height="9" rx="1" fill="#cfe6f8"/></svg>
    <div class="btn light" style="left:44px;top:94px;width:62px">Cancel</div>
    <div class="btn light" style="left:112px;top:94px;width:62px">OK</div>
  </div>
  <div class="btn ghost wide" style="top:225px">Create</div>
  <div class="nav"><svg width="219" height="12"><path d="M44 6l8-5v10z" fill="none" stroke="#555" stroke-width="1.4"/><circle cx="110" cy="6" r="5" fill="none" stroke="#555" stroke-width="1.4"/><rect x="166" y="1" width="10" height="10" fill="none" stroke="#555" stroke-width="1.4"/></svg></div>
</section>

<section class="screen" style="left:611.3px;top:494.6px">
  <div class="status"><svg width="22" height="7"><path d="M0 1h8L4 6z" fill="#222"/><path d="M10 6h5V1z" fill="#222"/><rect x="17" y="0" width="4" height="7" fill="#222"/></svg>12:30</div>
  <div class="logo">Recova</div>
  <div class="card blue" style="top:86px;height:96px">
    <svg class="idle-icon" width="76" height="56" viewBox="0 0 76 56"><path d="M38 8a20 20 0 0 1 20 20H38" fill="none" stroke="#fff" stroke-width="4"/><g fill="#fff"><circle cx="20" cy="28" r="2"/><circle cx="24" cy="17" r="2"/><circle cx="32" cy="10" r="2"/><circle cx="24" cy="40" r="2"/><circle cx="38" cy="46" r="2"/><circle cx="52" cy="40" r="2"/></g></svg>
    <p class="idle-text">Nothing to do at the moment.</p>
  </div>
  <div class="btn wide light" style="top:191px">View Reponses</div>
  <div class="tile drain faded"><svg width="50" height="50"><rect x="2" y="2" width="46" height="46" rx="4" fill="none" stroke="#1e88d8" stroke-width="3"/><g stroke="#1e88d8" stroke-width="3"><path d="M10 12h30M10 20h30M10 28h30M10 36h30"/></g></svg><span>Remind me to strip my drains</span></div>
  <div class="tile pills faded"><svg width="50" height="50"><rect x="2" y="14" width="26" height="14" rx="7" transform="rotate(40 15 21)" fill="#1e88d8"/><rect x="20" y="8" width="28" height="14" rx="7" transform="rotate(-40 34 15)" fill="#1e88d8"/><g fill="#1e88d8"><circle cx="24" cy="34" r="3"/><circle cx="18" cy="42" r="2.5"/><circle cx="30" cy="42" r="2.5"/><circle cx="24" cy="47" r="2"/></g></svg><span>Remind me to take my antibiotics</span></div>
  <div class="nav"><svg width="219" height="12"><path d="M44 6l8-5v10z" fill="none" stroke="#222" stroke-width="1.4"/><circle cx="110" cy="6" r="5" fill="none" stroke="#222" stroke-width="1.4"/><rect x="166" y="1" width="10" height="10" fill="none" stroke="#222" stroke-width="1.4"/></svg></div>
</section>

<section class="screen" style="left:754.6px;top:494.6px">
  <div class="status"><svg width="22" height="7"><path d="M0 1h8L4 6z" fill="#222"/><path d="M10 6h5V1z" fill="#222"/><rect x="17" y="0" width="4" height="7" fill="#222"/></svg>12:30</div>
  <div class="logo">Recova</div>
  <div class="reward-sheet"><svg style="left:22px" width="24" height="24" viewBox="0 0 24 24"><path d="M12 1l3.2 7 7.6.8-5.7 5.1 1.6 7.5L12 17.6 5.3 21.4l1.6-7.5L1.2 8.8l7.6-.8z" fill="var(--star)"/></svg></div>
  <div class="nav"><svg width="219" height="12"><path d="M44 6l8-5v10z" fill="none" stroke="#222" stroke-width="1.4"/><circle cx="110" cy="6" r="5" fill="none" stroke="#222" stroke-width="1.4"/><rect x="166" y="1" width="10" height="10" fill="none" stroke="#222" stroke-width="1.4"/></svg></div>
</section>

<!-- Row 4 -->
<section class="screen dark" style="left:38.5px;top:727px">
  <div class="status"><svg width="22" height="7"><path d="M0 1h8L4 6z" fill="#555"/><path d="M10 6h5V1z" fill="#555"/><rect x="17" y="0" width="4" height="7" fill="#555"/></svg>12:30</div>
  <div class="logo">Recova</div>
  <div class="card blue" style="top:86px;height:122px">
    <p class="summary">06/02/2018 08:42PM EDT<br>Drain Care<br>Difficulty: 7<br>Discomfort: ture<br>Amount of Fluid: 5<br>Color: Pink</p>
    <div class="dialog-actions"><div class="btn light" style="left:64px;width:62px">OK</div></div>
  </div>
  <div class="dim-panel" style="top:208px;height:90px"></div>
  <div class="nav"><svg width="219" height="12"><path d="M44 6l8-5v10z" fill="none" stroke="#555" stroke-width="1.4"/><circle cx="110" cy="6" r="5" fill="none" stroke="#555" stroke-width="1.4"/><rect x="166" y="1" width="10" height="10" fill="none" stroke="#555" stroke-width="1.4"/></svg></div>
</section>

<section class="screen dark" style="left:181.9px;top:727px">
  <div class="status"><svg width="22" height="7"><path d="M0 1h8L4 6z" fill="#555"/><path d="M10 6h5V1z" fill="#555"/><rect x="17" y="0" width="4" height="7" fill="#555"/></svg>12:30</div>
  <div class="logo">Recova</div>
  <div class="card" style="top:86px;height:122px">
    <p class="dialog-title">Time to strip your drains</p>
    <p class="dialog-body">It is time to take your antibiotics. Take tablet(s) with meals. Please follow the instructions provided by your physician.</p>
    <div class="dialog-actions"><div class="btn" style="left:32px;width:62px">Snooze</div><div class="btn" style="left:100px;width:62px">Done</div></div>
  </div>
  <div class="dim-panel" style="top:208px;height:90px"></div>
  <div class="nav"><svg width="219" height="12"><path d="M44 6l8-5v10z" fill="none" stroke="#555" stroke-width="1.4"/><circle cx="110" cy="6" r="5" fill="none" stroke="#555" stroke-width="1.4"/><rect x="166" y="1" width="10" height="10" fill="none" stroke="#555" stroke-width="1.4"/></svg></div>
</section>

<section class="screen" style="left:324.7px;top:727px">
  <div class="status"><svg width="22" height="7"><path d="M0 1h8L4 6z" fill="#222"/><path d="M10 6h5V1z" fill="#222"/><rect x="17" y="0" width="4" height="7" fill="#222"/></svg>12:30</div>
  <div class="logo">Recova</div>
  <h2 class="title">Did you take your medication with food?</h2>
  <div class="choice off" style="left:84px;top:155px">Yes</div>
  <div class="choice on" style="left:84px;top:228px">No</div>
  <div class="btn solo" style="top:329px">Next</div>
  <div class="nav"><svg width="219" height="12"><path d="M44 6l8-5v10z" fill="none" stroke="#222" stroke-width="1.4"/><circle cx="110" cy="6" r="5" fill="none" stroke="#222" stroke-width="1.4"/><rect x="166" y="1" width="10" height="10" fill="none" stroke="#222" stroke-width="1.4"/></svg></div>
</section>

<section class="screen" style="left:468px;top:727px">
  <div class="status"><svg width="22" height="7"><path d="M0 1h8L4 6z" fill="#222"/><path d="M10 6h5V1z" fill="#222"/><rect x="17" y="0" width="4" height="7" fill="#222"/></svg>12:30</div>
  <div class="logo">Recova</div>
  <h2 class="title">Did you have any stomach upest after taking the medication?</h2>
  <div class="choice on" style="left:49px;top:189px">Yes</div>
  <div class="choice off" style="left:116px;top:189px">No</div>
  <div class="btn prev" style="top:329px">Previous</div>
  <div class="btn next" style="top:329px">Complete</div>
  <div class="nav"><svg width="219" height="12"><path d="M44 6l8-5v10z" fill="none" stroke="#222" stroke-width="1.4"/><circle cx="110" cy="6" r="5" fill="none" stroke="#222" stroke-width="1.4"/><rect x="166" y="1" width="10" height="10" fill="none" stroke="#222" stroke-width="1.4"/></svg></div>
</section>

<section class="screen" style="left:611.3px;top:727px">
  <div class="status"><svg width="22" height="7"><path d="M0 1h8L4 6z" fill="#222"/><path d="M10 6h5V1z" fill="#222"/><rect x="17" y="0" width="4" height="7" fill="#222"/></svg>12:30</div>
  <div class="logo">Recova</div>
  <h2 class="title">Did you have any stomach upest after taking the medication?</h2>
  <div class="choice on" style="left:49px;top:189px">Yes</div>
  <div class="choice off" style="left:116px;top:189px">No</div>
  <div class="btn prev" style="top:329px">Previous</div>
  <div class="btn next" style="top:329px">Complete</div>
  <div class="nav"><svg width="219" height="12"><path d="M44 6l8-5v10z" fill="none" stroke="#222" stroke-width="1.4"/><circle cx="110" cy="6" r="5" fill="none" stroke="#222" stroke-width="1.4"/><rect x="166" y="1" width="10" height="10" fill="none" stroke="#222" stroke-width="1.4"/></svg></div>
</section>

<section class="screen" style="left:754.6px;top:727px">
  <div class="status"><svg width="22" height="7"><path d="M0 1h8L4 6z" fill="#222"/><path d="M10 6h5V1z" fill="#222"/><rect x="17" y="0" width="4" height="7" fill="#222"/></svg>12:30</div>
  <div class="logo">Recova</div>
  <h2 class="title">Did you take your medication with food?</h2>
  <div class="choice off" style="left:84px;top:155px">Yes</div>
  <div class="choice on" style="left:84px;top:228px">No</div>
  <div class="btn solo" style="top:329px">Next</div>
  <div class="nav"><svg width="219" height="12"><path d="M44 6l8-5v10z" fill="none" stroke="#222" stroke-width="1.4"/><circle cx="110" cy="6" r="5" fill="none" stroke="#222" stroke-width="1.4"/><rect x="166" y="1" width="10" height="10" fill="none" stroke="#222" stroke-width="1.4"/></svg></div>
</section>

<!-- Row 5 -->
<section class="screen dark" style="left:38.5px;top:959.3px">
  <div class="status"><svg width="22" height="7"><path d="M0 1h8L4 6z" fill="#555"/><path d="M10 6h5V1z" fill="#555"/><rect x="17" y="0" width="4" height="7" fill="#555"/></svg>12:30</div>
  <div class="logo">Recova</div>
  <div class="choice on" style="left:50px;top:190px;opacity:.3">Yes</div>
  <div class="card" style="top:86px;height:122px">
    <p class="dialog-title">Congratulations</p>
    <p class="dialog-body">You have earned another diamond!<br>Keep up the good work!</p>
    <svg style="position:absolute;left:89px;top:64px" width="12" height="14" viewBox="0 0 12 14"><path d="M6 0l6 7-6 7-6-7z" fill="var(--gem)"/><path d="M6 0v14M0 7h12" stroke="#a8ecbf" stroke-width=".8"/></svg>
    <div class="dialog-actions"><div class="btn" style="left:64px;width:62px">OK</div></div>
  </div>
  <div class="btn ghost prev" style="top:329px">Previous</div>
  <div class="btn ghost next" style="top:329px">Complete</div>
  <div class="nav"><svg width="219" height="12"><path d="M44 6l8-5v10z" fill="none" stroke="#555" stroke-width="1.4"/><circle cx="110" cy="6" r="5" fill="none" stroke="#555" stroke-width="1.4"/><rect x="166" y="1" width="10" height="10" fill="none" stroke="#555" stroke-width="1.4"/></svg></div>
</section>

<section class="screen" style="left:181.9px;top:959.3px">
  <div class="status"><svg width="22" height="7"><path d="M0 1h8L4 6z" fill="#222"/><path d="M10 6h5V1z" fill="#222"/><rect x="17" y="0" width="4" height="7" fill="#222"/></svg>12:30</div>
  <div class="logo">Recova</div>
  <div class="reward-sheet">
    <svg style="left:16px" width="24" height="24" viewBox="0 0 24 24"><path d="M12 1l3.2 7 7.6.8-5.7 5.1 1.6 7.5L12 17.6 5.3 21.4l1.6-7.5L1.2 8.8l7.6-.8z" fill="var(--star)"/></svg>
    <svg style="left:52px" width="20" height="24" viewBox="0 0 12 14"><path d="M6 0l6 7-6 7-6-7z" fill="var(--gem)"/><path d="M6 0v14M0 7h12" stroke="#a8ecbf" stroke-width=".8"/></svg>
  </div>
  <div class="nav"><svg width="219" height="12"><path d="M44 6l8-5v10z" fill="none" stroke="#222" stroke-width="1.4"/><circle cx="110" cy="6" r="5" fill="none" stroke="#222" stroke-width="1.4"/><rect x="166" y="1" width="10" height="10" fill="none" stroke="#222" stroke-width="1.4"/></svg></div>
</section>

<section class="screen dark" style="left:324.7px;top:959.3px">
  <div class="status"><svg width="22" height="7"><path d="M0 1h8L4 6z" fill="#555"/><path d="M10 6h5V1z" fill="#555"/><rect x="17" y="0" width="4" height="7" fill="#555"/></svg>12:30</div>
  <div class="logo">Recova</div>
  <div class="card blue" style="top:86px;height:122px">
    <p class="summary">06/02/2018 08:42PM EDT<br>Drain Care<br>Difficulty: 7<br>Discomfort: ture<br>Amount of Fluid: 5<br>Color: Pink</p>
    <div class="dialog-actions"><div class="btn light" style="left:64px;width:62px">OK</div></div>
  </div>
  <div class="dim-panel" style="top:208px;height:90px"></div>
  <div class="nav"><svg width="219" height="12"><path d="M44 6l8-5v10z" fill="none" stroke="#555" stroke-width="1.4"/><circle cx="110" cy="6" r="5" fill="none" stroke="#555" stroke-width="1.4"/><rect x="166" y="1" width="10" height="10" fill="none" stroke="#555" stroke-width="1.4"/></svg></div>
</section>

<section class="screen dark" style="left:468px;top:959.3px">
  <div class="status"><svg width="22" height="7"><path d="M0 1h8L4 6z" fill="#555"/><path d="M10 6h5V1z" fill="#555"/><rect x="17" y="0" width="4" height="7" fill="#555"/></svg>12:30</div>
  <div class="logo">Recova</div>
  <div class="card blue" style="top:86px;height:122px">
    <p class="summary">06/02/2018 08:45 PM EDT<br>Antibiotics<br>Took w/Food: false<br>Upest Stomach: true</p>
    <div class="dialog-actions"><div class="btn light" style="left:64px;width:62px">OK</div></div>
  </div>
  <div class="dim-panel" style="top:208px;height:90px"></div>
  <div class="nav"><svg width="219" height="12"><path d="M44 6l8-5v10z" fill="none" stroke="#555" stroke-width="1.4"/><circle cx="110" cy="6" r="5" fill="none" stroke="#555" stroke-width="1.4"/><rect x="166" y="1" width="10" height="10" fill="none" stroke="#555" stroke-width="1.4"/></svg></div>
</section>

<section class="screen splash" style="left:611.3px;top:959.3px">
  <div class="status"><svg width="22" height="7"><path d="M0 1h8L4 6z" fill="#222"/><path d="M10 6h5V1z" fill="#222"/><rect x="17" y="0" width="4" height="7" fill="#222"/></svg>12:30</div>
  <div class="splash-ring">Recova</div>
  <div class="nav"><svg width="219" height="12"><path d="M44 6l8-5v10z" fill="none" stroke="#222" stroke-width="1.4"/><circle cx="110" cy="6" r="5" fill="none" stroke="#222" stroke-width="1.4"/><rect x="166" y="1" width="10" height="10" fill="none" stroke="#222" stroke-width="1.4"/></svg></div>
</section>

</div>
</body>
</html>
```